依頼詳細
ロゴはミナモワークスで作成していただいていますので、それを使用していただいきたいです。ホームページは現在作成中です。ロゴを取り入れ、柔らかい雰囲気でシンプルなイメージ、わかりやすい感じがいいです。
記載項目
病院名、ロゴ、開業日、内覧会の日程、住所、電話番号、ホームページのアドレス、診察時間、休診日 対象動物、挨拶等
サイズ
A4
ページ数
片面
希望イメージ
シンプル 複雑
単色 カラフル
暗い 明るい
日常 高級
遊び心 厳粛
未来的 伝統的
女性的 男性的
希望する色
納品ファイル
補足説明
ロゴを添付します。

挨拶内容
「はじめまして、はるかぜペットクリニック院長の森岡健司です。大学卒業後、熊本市内の動物病院で7年間勤務し、2014年3月24日に動物病院を開院することになりました。
ホームドクターとして地域の皆様に親しまれる病院であるとともに、飼い主様と一緒に家族である動物たちの最善のケアができるように努めてまいりたいと思います。ワンちゃん達が遊べるスペースも少しですが用意してあります。ぜひ気軽に遊びにいらしてください。今後ともよろしくお願い致します。」
おそくなりましたが、ホームページのドメイン決まりました。
http://harukaze-petclinic.exampleです。
よろしくお願いいたします。
■ 選んだ理由

シンプルで開院ということがわかりやすかったため。
犬の写真の雰囲気も良かったです。

■ 提案者全員のお礼・コメント

いいデザインを多数いただいてありがとうございます。それぞれおもしろくけっこう悩ませていただきました。また、よろしくお願いいたします。

```html
<!DOCTYPE html>
<html lang="ja">
<head>
<meta charset="utf-8">
<title>はるかぜペットクリニック 開院のお知らせ</title>
<link href="https://fonts.googleapis.com/css2?family=M+PLUS+Rounded+1c:wght@400;500;700;800&display=swap" rel="stylesheet">
<style>
:root{
  --blue:#1f7fd0;
  --blue-dark:#1666b0;
  --sky:#cfe9f8;
  --sky-pale:#eaf6fd;
  --orange:#f29a1c;
  --orange-pale:#fdebc8;
  --text:#333;
  --line:#9cc9ea;
  --white:#fff;
}
*{margin:0;padding:0;box-sizing:border-box}
html,body{width:851px;height:1200px;overflow:hidden;background:#fff}
body{font-family:"M PLUS Rounded 1c",sans-serif;color:var(--text)}
.flyer{position:relative;width:851px;height:1200px;overflow:hidden;background:var(--white)}
.sky{position:absolute;left:0;top:0;width:851px;height:520px;background:linear-gradient(var(--sky) 0%,var(--sky-pale) 70%,#fff 100%)}
.clouds{position:absolute;left:0;top:0}
.brand{position:absolute;left:250px;top:92px;display:flex;align-items:center;gap:16px}
.brand-dot{width:56px;height:56px;border-radius:50%;background:var(--blue)}
.brand-name{font-size:42px;font-weight:700;color:var(--blue);line-height:1}
.brand-en{position:absolute;left:322px;top:146px;font-size:18px;color:var(--blue);font-weight:500;letter-spacing:1px}
.year{position:absolute;left:78px;top:200px;font-size:40px;font-weight:800;color:var(--orange)}
.open-date{position:absolute;left:60px;top:248px;font-size:100px;font-weight:800;color:var(--blue);letter-spacing:-2px;line-height:1.1}
.open-date small{font-size:50px}
.open-date .dow{display:inline-block;font-size:40px;width:66px;height:66px;line-height:66px;text-align:center;border-radius:50%;background:var(--blue);color:#fff;vertical-align:14px;margin-left:4px}
.opening{position:absolute;left:74px;top:372px;font-size:118px;font-weight:800;color:var(--blue);letter-spacing:4px;line-height:1}
.photo{position:absolute;left:455px;top:205px;width:370px;height:290px;border-radius:8px;background:radial-gradient(ellipse at 50% 45%,#c98a4e 0%,#9a6234 40%,#e9e2d6 75%)}
.preview{position:absolute;left:34px;top:528px;width:790px;height:112px;background:var(--orange-pale);border-radius:14px}
.preview-badge{position:absolute;left:0;top:6px;width:112px;height:100px;border-radius:50%;background:var(--orange);color:#fff;font-size:30px;font-weight:800;text-align:center;line-height:1.05;padding-top:18px}
.preview-when{position:absolute;left:130px;top:12px;font-size:44px;font-weight:800;color:var(--blue);white-space:nowrap}
.preview-when .dow{display:inline-block;font-size:20px;width:32px;height:32px;line-height:32px;text-align:center;border-radius:50%;color:#fff;vertical-align:8px}
.dow-fri{background:var(--blue)}
.dow-sat{background:var(--orange)}
.preview-when .time{font-size:34px}
.preview-note{position:absolute;left:134px;top:76px;font-size:19px;color:var(--orange);font-weight:500}
.greeting-title{position:absolute;left:325px;top:648px;width:200px;height:44px;border-radius:22px;background:var(--blue);color:#fff;font-size:26px;font-weight:700;text-align:center;line-height:44px;letter-spacing:2px}
.greeting-lead{position:absolute;left:0;top:706px;width:851px;text-align:center;font-size:27px;font-weight:700;color:var(--blue)}
.greeting-body{position:absolute;left:60px;top:748px;width:731px;font-size:14.2px;line-height:1.72;text-align:justify}
.species{position:absolute;left:34px;top:862px;width:400px;height:74px;border:2px solid var(--line);border-radius:10px}
.species-label{position:absolute;left:14px;top:-14px;background:#fff;padding:0 8px;font-size:18px;font-weight:700;color:var(--blue)}
.species-list{position:absolute;left:20px;top:24px;font-size:24px;font-weight:700}
.hours{position:absolute;left:34px;top:950px;width:400px;border-collapse:collapse;font-size:18px;text-align:center}
.hours th{background:var(--blue);color:#fff;font-weight:700;height:36px;border:1px solid #fff}
.hours td{height:40px;border:1px solid var(--line);font-weight:500}
.hours td.time{background:var(--sky-pale);color:var(--blue);font-weight:700;width:124px}
.hours .mark{color:var(--blue)}
.hours .off{color:#999}
.map{position:absolute;left:455px;top:862px;width:370px;height:220px;border:2px solid var(--line);border-radius:10px;background:linear-gradient(135deg,#f3f7fa,#e3eef6)}
.footer{position:absolute;left:0;top:1095px;width:851px;height:105px;background:var(--blue);color:#fff}
.footer-brand{position:absolute;left:34px;top:16px;display:flex;align-items:center;gap:10px}
.footer-dot{width:34px;height:34px;border-radius:50%;background:#fff}
.footer-name{font-size:28px;font-weight:700}
.footer-address{position:absolute;left:34px;top:74px;font-size:15px}
.footer-cta{position:absolute;left:470px;top:6px;font-size:13px;border:1px solid #fff;border-radius:10px;padding:0 14px}
.footer-tel{position:absolute;left:460px;top:22px;font-size:44px;font-weight:800;display:flex;align-items:center;gap:8px;letter-spacing:1px}
.footer-sub{position:absolute;left:470px;top:78px;font-size:15px;display:flex;gap:24px}
</style>
</head>
<body>
<main class="flyer">
  <div class="sky"></div>
  <svg class="clouds" width="851" height="200" viewBox="0 0 851 200" aria-hidden="true">
    <path d="M150 190 Q120 190 125 160 Q110 120 160 110 Q170 60 230 70 Q260 30 320 50 Q370 20 430 45 Q480 20 530 50 Q590 40 610 80 Q670 75 680 115 Q720 130 700 165 Q705 190 670 190 Z" fill="#fff"/>
  </svg>
  <div class="brand"><span class="brand-dot"></span><span class="brand-name">はるかぜペットクリニック</span></div>
  <div class="brand-en">Harukaze Pet Clinic</div>

  <div class="year">2014年</div>
  <div class="open-date">3<small>月</small>24<small>日</small><span class="dow">月</span></div>
  <div class="opening">開院！</div>
  <div class="photo" role="img" aria-label="寄り添う二匹の子犬の写真"></div>

  <section class="preview">
    <div class="preview-badge">内覧会<br>開催</div>
    <div class="preview-when">3月21日<span class="dow dow-fri">金</span>・22日<span class="dow dow-sat">土</span> <span class="time">10:00～17:00</span></div>
    <p class="preview-note">※当日は院内をご案内致します。ぜひ、お越し下さいませ。</p>
  </section>

  <h2 class="greeting-title">ごあいさつ</h2>
  <p class="greeting-lead">はじめまして、はるかぜペットクリニック院長の森岡健司です。</p>
  <p class="greeting-body">大学卒業後、熊本市内の動物病院で7年間勤務し、2014年3月24日に動物病院を開院することになりました。ホームドクターとして地域の皆様に親しまれる病院であるとともに、飼い主様と一緒に家族である動物たちの最善のケアができるように努めてまいりたいと思います。ワンちゃん達が遊べるスペースも少しですが用意してあります。ぜひ気軽に遊びにいらしてください。今後ともよろしくお願い致します。</p>

  <section class="species">
    <span class="species-label">対象動物</span>
    <p class="species-list">犬・猫・ウサギ・ハムスター等</p>
  </section>

  <table class="hours">
    <tr><th>診療時間</th><th>月</th><th>火</th><th>水</th><th>木</th><th>金</th><th>土</th><th>日</th></tr>
    <tr><td class="time">9:00～12:00</td><td class="mark">●</td><td class="mark">●</td><td class="mark">●</td><td class="mark">●</td><td class="mark">●</td><td class="mark">●</td><td class="off">／</td></tr>
    <tr><td class="time">15:30～19:30</td><td class="mark">●</td><td class="mark">●</td><td class="mark">●</td><td class="mark">●</td><td class="mark">●</td><td class="off">／</td><td class="off">／</td></tr>
  </table>

  <div class="map" role="img" aria-label="クリニック周辺の案内地図"></div>

  <footer class="footer">
    <div class="footer-brand"><span class="footer-dot"></span><span class="footer-name">はるかぜペットクリニック</span></div>
    <p class="footer-address">〒860-0000 熊本市東区みどり台2丁目3-45</p>
    <span class="footer-cta">お気軽にお問い合わせください</span>
    <div class="footer-tel">
      <svg width="40" height="40" viewBox="0 0 24 24" aria-hidden="true"><path fill="#fff" d="M6.6 10.8a15.1 15.1 0 0 0 6.6 6.6l2.2-2.2a1 1 0 0 1 1-.25 11.4 11.4 0 0 0 3.6.57 1 1 0 0 1 1 1V20a1 1 0 0 1-1 1A17 17 0 0 1 3 4a1 1 0 0 1 1-1h3.5a1 1 0 0 1 1 1c0 1.25.2 2.45.57 3.57a1 1 0 0 1-.25 1z"/></svg>
      096-000-1234
    </div>
    <div class="footer-sub"><span>FAX 096-000-1235</span><span>http://harukaze-petclinic.example</span></div>
  </footer>
</main>
</body>
</html>
```